Business Card Design

We are a commercial real estate brokerage in San Francisco, leasing office buildings downtown.
I would like a clean, elegant look. Simple but powerful .

Industry/Entity Type

Business

Contact Information for Business Card

Colin Farrow
lic# 07281549
415.555.0172
colin@tarvo-commercial.example
tarvo-commercial.example

```html
<!DOCTYPE html>
<html lang="en">
<head>
<meta charset="utf-8">
<title>Tarvo Commercial – Business Card</title>
<link href="https://fonts.googleapis.com/css2?family=Roboto:wght@400;500;700&display=swap" rel="stylesheet">
<style>
  :root {
    --backdrop: #ece9e4;
    --card: #ffffff;
    --brand: #6e7e97;
    --text-grey: #7d8391;
    --icon-grey: #9a9ea6;
    --mark: #5a5d63;
  }
  * { margin: 0; padding: 0; box-sizing: border-box; }
  html, body {
    width: 1200px;
    height: 695px;
    overflow: hidden;
    background: var(--backdrop);
    font-family: "Roboto", Arial, sans-serif;
  }
  .canvas {
    position: relative;
    width: 1200px;
    height: 695px;
  }
  .card {
    position: absolute;
    left: 340px;
    top: 195px;
    width: 520px;
    height: 305px;
    background: var(--card);
    box-shadow: 0 1px 3px rgba(0,0,0,0.12);
  }
  .brand {
    position: absolute;
    left: 38px;
    top: 58px;
    display: flex;
    align-items: center;
    gap: 12px;
  }
  .brand-square {
    width: 28px;
    height: 28px;
    background: var(--mark);
  }
  .brand-name {
    font-size: 26px;
    font-weight: 500;
    letter-spacing: 0.5px;
    color: var(--brand);
    line-height: 1;
  }
  .contact {
    position: absolute;
    left: 276px;
    top: 151px;
  }
  .contact-name {
    font-size: 16px;
    font-weight: 700;
    color: var(--brand);
    letter-spacing: 0.2px;
    margin-bottom: 7px;
  }
  .licence {
    font-size: 14px;
    color: var(--text-grey);
    margin-bottom: 4px;
  }
  .contact-line {
    display: flex;
    align-items: center;
    gap: 6px;
    font-size: 14px;
    color: var(--brand);
    height: 18px;
    margin-bottom: 8px;
  }
  .contact-icon {
    width: 9px;
    height: 9px;
    flex: none;
  }
</style>
</head>
<body>
<div class="canvas">
  <div class="card">
    <div class="brand">
      <div class="brand-square"></div>
      <div class="brand-name">TARVO COMMERCIAL</div>
    </div>

    <div class="contact">
      <div class="contact-name">COLIN FARROW</div>
      <div class="licence">lic# 07281549</div>

      <div class="contact-line">
        <svg class="contact-icon" viewBox="0 0 10 10" aria-hidden="true">
          <circle cx="5" cy="5" r="5" fill="var(--icon-grey)"/>
          <path d="M3.3 2.6 L4.2 3.6 L3.8 4.2 Q4.5 5.6 5.8 6.2 L6.4 5.8 L7.4 6.7 L6.8 7.4 Q3.2 6.8 2.6 3.2 Z" fill="#fff"/>
        </svg>
        <span>415.555.0172</span>
      </div>

      <div class="contact-line">
        <svg class="contact-icon" viewBox="0 0 10 10" aria-hidden="true">
          <circle cx="5" cy="5" r="5" fill="var(--icon-grey)"/>
          <rect x="2.4" y="3.2" width="5.2" height="3.6" fill="none" stroke="#fff" stroke-width="0.8"/>
          <path d="M2.4 3.2 L5 5.2 L7.6 3.2" fill="none" stroke="#fff" stroke-width="0.8"/>
        </svg>
        <span>colin@tarvo-commercial.example</span>
      </div>

      <div class="contact-line">
        <svg class="contact-icon" viewBox="0 0 10 10" aria-hidden="true">
          <circle cx="5" cy="5" r="4.4" fill="none" stroke="var(--icon-grey)" stroke-width="0.9"/>
          <ellipse cx="5" cy="5" rx="1.9" ry="4.4" fill="none" stroke="var(--icon-grey)" stroke-width="0.7"/>
          <line x1="0.6" y1="5" x2="9.4" y2="5" stroke="var(--icon-grey)" stroke-width="0.7"/>
        </svg>
        <span>tarvo-commercial.example</span>
      </div>
    </div>
  </div>
</div>
</body>
</html>
```